2 page flyer for a turf supply company. MERIDELL TURF SOLUTIONS

Design a marketing flyer to be distributed to landscaping contractors, councils, and private users.
I have attached a FileCrate link that holds the logo files, copy, and brand guidelines and images.
I am wanting the brochure to be 2 pages, which can be sent as a pdf or printed double-sided. I would like a modern, professional look using the colours from the brand guidelines. We are designing a new website so this brochure will be found on the website as well as sent to clients. I have uploaded the copy, a logo, and brand guidelines. The link to more photos and logos are found on the FileCrate link below.
https://www.filecrate-share.example/scl/fo/qwk83zmtlpdnv5b2hxcrt/h?rlkey=914vbnkstpqwe7yz2mcx8lf4d&dl=0
Here is the link to the current website. https://meridellgroup.com.au/
New one coming.

Target Market(s)

The decision makers at councils, landscape businesses and land developers

Industry/Entity Type

landscaping companies and councils

Font styles to use
Sans Serif

Requirements
Must have
• must be eye catching and easy to read
Nice to have
• Bold headings

```html
<!DOCTYPE html>
<html lang="en">
<head>
<meta charset="utf-8">
<title>Meridell Turf Solutions – Turf Varieties</title>
<link rel="stylesheet" href="https://fonts.googleapis.com/css2?family=Bodoni+Moda:opsz,wght@6..96,400;6..96,500&display=swap">
<style>
  :root {
    --page-bg: #eef6fa;
    --ink: #111418;
    --band: #1a5a7d;
    --photo-sky: #6fa6d6;
    --photo-grass: #6f9e45;
    --photo-grass-deep: #4f8a2e;
  }
  * { margin: 0; padding: 0; box-sizing: border-box; }
  html, body { width: 846px; height: 1200px; overflow: hidden; }
  body {
    background: var(--page-bg);
    color: var(--ink);
    font-family: "Bodoni Moda", "Libre Bodoni", Georgia, serif;
    font-optical-sizing: auto;
    font-weight: 400;
    position: relative;
  }
  .varieties {
    position: absolute;
    left: 46px;
    top: 48px;
    width: 758px;
  }
  .section-title {
    font-size: 19.5px;
    font-weight: 400;
    letter-spacing: 0.2px;
    line-height: 24px;
    margin-bottom: 12px;
  }
  .variety {
    font-size: 15.4px;
    font-weight: 400;
    line-height: 24.6px;
  }
  .variety-name {
    font-size: 19.4px;
    font-weight: 500;
  }
  .photos {
    position: absolute;
    top: 433px;
    left: 0;
    width: 846px;
    height: 400px;
  }
  .photo { position: absolute; top: 0; height: 400px; }
  .photo-skatepark {
    left: 0; width: 414px;
    background: linear-gradient(180deg, var(--photo-sky) 0%, var(--photo-grass) 100%);
  }
  .photo-field {
    left: 434px; width: 412px;
    background: linear-gradient(180deg, var(--photo-grass) 0%, var(--photo-grass-deep) 100%);
  }
  .services {
    position: absolute;
    left: 46px;
    top: 852px;
  }
  .services .section-title { margin-bottom: 11px; }
  .service-list { list-style: none; }
  .service-list li {
    position: relative;
    padding-left: 102px;
    font-size: 15.4px;
    font-weight: 400;
    line-height: 29.9px;
  }
  .service-list li::before {
    content: "";
    position: absolute;
    left: 56px;
    top: 13px;
    width: 5px; height: 5px;
    border-radius: 50%;
    background: var(--ink);
  }
  .footer-band {
    position: absolute;
    left: 0; bottom: 0;
    width: 846px; height: 37px;
    background: var(--band);
  }
</style>
</head>
<body>
  <section class="varieties">
    <h2 class="section-title">TURF VARIETIES GROWN AND AVAILABLE:</h2>
    <p class="variety"><span class="variety-name">Santa Anna Couch:</span> Known for its resilience and fine texture, Santa Anna Couch is a versatile turf variety ideal for creating lush, green landscapes that can withstand various environmental conditions.</p>
    <p class="variety"><span class="variety-name">Wintergreen Couch:</span> Wintergreen Couch is prized for its vibrant green colour and dense growth, making it a popular choice for lawns and sports fields, providing a soft and inviting surface.</p>
    <p class="variety"><span class="variety-name">Kikuyu:</span> Renowned for its rapid growth, durability, and ability to thrive in various climates, Kikuyu turf is a popular choice for lawns, sports fields, and recreational areas, providing a resilient and vibrant green surface.</p>
    <p class="variety"><span class="variety-name">Oversown Rye Grass Blends (Oversown to Order):</span> Our Oversown Rye Grass Blends are tailored to order, offering a flexible solution for enhancing turf durability and maintaining a lush appearance, especially during colder seasons.</p>
  </section>

  <div class="photos">
    <div class="photo photo-skatepark" role="img" aria-label="Photo: skate park with freshly laid turf in the foreground"></div>
    <div class="photo photo-field" role="img" aria-label="Photo: large open sports field covered in green turf"></div>
  </div>

  <section class="services">
    <h2 class="section-title">MERIDELL TURF SOLUTIONS SERVICES:</h2>
    <ul class="service-list">
      <li>Turf supply</li>
      <li>Domestic &amp; commercial sales</li>
      <li>Thick cut turf, supplied in either maxi rolls or standard turf rolls</li>
      <li>Contract growing</li>
      <li>Pick up or delivery</li>
    </ul>
  </section>

  <div class="footer-band"></div>
</body>
</html>
```